Simple landing page for Brindleys cookbook

I need a one page landingpage where customers can order the cookbook.
This is a cookbook of a collection of recipes from our deli that we used to run.
I need a landing page where customers can come and order the book. I also need it coded. I already have the domain through hostmoxa.
I can send the file of the book through wetransfer. It's too big to upload here. Just so you get the feel that I am looking for.
I attached a simple text as an introduction to the page. But I am open to any suggestions. I want it all to be about the experience that we are sharing the recipes with everybody and that it's for sale. The book is $29.99, shipping included.
Customers have to be able to click and buy the book from it.

Coding

Coded - Design and coding required

Number of Pages Required

1 page

Font styles to use
Sans Serif

Requirements
Must have
• Same colors as the cookbook

```html
<!DOCTYPE html>
<html lang="en">
<head>
<meta charset="utf-8">
<title>Brindleys Sandwiches – Cookbook</title>
<link href="https://fonts.googleapis.com/css2?family=Oswald:wght@200;300;400;500;600;700&family=Roboto+Slab:wght@300;400&display=swap" rel="stylesheet">
<style>
:root{
  --orange:#f48c1c;
  --orange-deep:#f05a1a;
  --dark:#1b1f22;
  --dark-2:#202427;
  --white:#ffffff;
  --yellow:#f7b51c;
}
*{margin:0;padding:0;box-sizing:border-box}
html,body{width:1200px;height:1145px;overflow:hidden;background:var(--dark)}
body{position:relative;font-family:'Roboto Slab',serif;color:var(--white)}
.abs{position:absolute}

/* hero */
.hero{position:absolute;left:0;top:0;width:1200px;height:532px;background:radial-gradient(circle at 30% 40%,#2a2e31,var(--dark) 70%)}
.hero__orange-top{left:600px;top:0;width:600px;height:267px;background:var(--orange)}
.brand{left:130px;top:18px;font-family:'Oswald',sans-serif;font-weight:600;font-size:17px;line-height:19px;letter-spacing:.5px;text-transform:uppercase;color:var(--white);width:110px}
.tag-strip{left:0;top:224px;width:35px;height:166px;background:var(--orange)}
.tag-edge{left:0;top:144px;width:35px;height:80px;border-top:2px solid var(--orange)}
.tag{font-family:'Oswald',sans-serif;color:var(--white);padding-left:93px;line-height:1}
.tag--fresh{left:35px;top:144px;width:316px;height:83px;background:var(--orange);font-weight:200;font-size:62px;letter-spacing:11px;padding-top:8px}
.tag--and{left:35px;top:228px;width:236px;height:80px;border-right:2px solid var(--orange);border-bottom:2px solid var(--orange);font-weight:300;font-size:62px;letter-spacing:9px;padding-top:6px}
.tag--tasty{left:35px;top:309px;width:336px;height:81px;border:2px solid var(--orange);border-left:none;font-weight:600;font-size:62px;letter-spacing:17px;padding-top:6px}
.social{left:130px;top:424px;display:flex;gap:11px}
.social span{width:30px;height:30px;border-radius:50%;background:#2c3033;display:block}
.book{left:450px;top:46px;width:300px;height:440px;border-radius:3px;background:linear-gradient(180deg,#eef2f5 0%,#e7d3b0 45%,#b67a3e 70%,#eae7e2 100%);box-shadow:0 8px 20px rgba(0,0,0,.5)}
.book-line{left:600px;top:486px;width:2px;height:46px;background:var(--orange)}
.garnish{border-radius:50%}
.garnish--basil{left:310px;top:390px;width:130px;height:120px;background:radial-gradient(circle,#4d8a2a,#2e5e1a 70%,transparent 72%)}
.garnish--garlic{left:255px;top:78px;width:70px;height:55px;background:radial-gradient(circle,#d8a3ad,#a44e63 70%,transparent 72%)}
.garnish--tomato{left:760px;top:410px;width:100px;height:100px;background:radial-gradient(circle,#e34b2a,#b3180f 68%,transparent 70%)}
.garnish--mushroom{left:1010px;top:282px;width:120px;height:110px;background:radial-gradient(circle,#f1e5d3,#c9ad8a 60%,transparent 62%)}
.garnish--chili{left:775px;top:18px;width:110px;height:40px;background:radial-gradient(ellipse,#d2281a,#8e1208 65%,transparent 67%)}
.offer-title{right:127px;top:72px;font-family:'Oswald',sans-serif;font-weight:700;font-size:58px;line-height:1;text-align:right}
.offer-sub{right:127px;top:146px;width:320px;font-family:'Oswald',sans-serif;font-weight:500;font-size:25px;line-height:30px;text-align:right}
.btn{left:771px;top:288px;width:168px;height:41px;border-radius:21px;background:linear-gradient(180deg,var(--orange),var(--orange-deep));border-bottom:3px solid var(--white);font-family:'Oswald',sans-serif;font-weight:600;font-size:18px;letter-spacing:2px;color:var(--white);text-align:center;line-height:38px;text-decoration:none}
.arrow{top:244px}
.shipping{right:127px;top:420px;text-align:right;font-family:'Oswald',sans-serif;line-height:1}
.shipping__label{font-weight:300;font-style:italic;font-size:38px}
.shipping__price{font-weight:700;font-size:46px;color:var(--orange);margin-top:2px}

/* story */
.story{position:absolute;left:0;top:532px;width:1200px;height:556px;background:var(--dark)}
.story__orange-left{left:0;top:532px;width:107px;height:101px;background:var(--orange)}
.story__orange-right{left:830px;top:700px;width:370px;height:388px;background:var(--orange)}
.frame-square{left:98px;top:555px;width:30px;height:28px;border:1px solid #8a8a8a}
.frame-tilt{left:26px;top:620px;width:80px;height:76px;border:1px solid var(--white);transform:rotate(20deg)}
.story__heading{left:130px;top:590px;font-family:'Oswald',sans-serif;line-height:1}
.story__kicker{font-weight:300;font-size:33px;display:block}
.story__title{font-weight:600;font-size:38px;display:block;margin-top:12px}
.story__title em{font-style:normal;color:var(--orange)}
.story__text{left:130px;top:696px;width:548px;font-size:12.5px;line-height:19.5px}
.story__lead{font-weight:400;width:450px;margin-bottom:22px}
.story__text p{font-weight:300;margin-bottom:11px}
.burger{left:693px;top:607px;width:457px;height:428px;border-radius:48% 48% 30% 30%;background:radial-gradient(ellipse at 50% 40%,#f0b55c,#c76a2a 45%,#5a2e18 62%,#4c8a2a 75%,#e9c47e 88%,transparent 90%)}

/* footer */
.footer{position:absolute;left:0;top:1088px;width:1200px;height:57px;background:var(--orange);text-align:center;font-size:12px;letter-spacing:1.3px;line-height:57px}
</style>
</head>
<body>
<section class="hero">
  <div class="abs hero__orange-top"></div>
  <div class="abs brand">Brindleys Sandwiches</div>
  <div class="abs tag-edge"></div>
  <div class="abs tag-strip"></div>
  <div class="abs tag tag--fresh">FRESH</div>
  <div class="abs tag tag--and">AND</div>
  <div class="abs tag tag--tasty">TASTY</div>
  <div class="abs social" aria-label="Social links"><span></span><span></span><span></span></div>
  <div class="abs garnish garnish--garlic" role="img" aria-label="Garlic clove"></div>
  <div class="abs garnish garnish--basil" role="img" aria-label="Fresh basil leaves"></div>
  <div class="abs book" role="img" aria-label="Brindleys Sandwiches cookbook cover with a sandwich photo"></div>
  <div class="abs book-line"></div>
  <div class="abs garnish garnish--chili" role="img" aria-label="Red chili pepper"></div>
  <h1 class="abs offer-title">28 DELICOUS</h1>
  <p class="abs offer-sub">Recipes Sandwiches, Sauces and Burgers</p>
  <svg class="abs arrow" style="left:762px" width="30" height="42" viewBox="0 0 30 42"><path d="M8 2 C0 14 4 28 18 32" fill="none" stroke="var(--yellow)" stroke-width="5"/><path d="M14 24 L24 34 L11 38 Z" fill="var(--yellow)"/></svg>
  <svg class="abs arrow" style="left:922px" width="30" height="42" viewBox="0 0 30 42"><path d="M22 2 C30 14 26 28 12 32" fill="none" stroke="var(--yellow)" stroke-width="5"/><path d="M16 24 L6 34 L19 38 Z" fill="var(--yellow)"/></svg>
  <a class="abs btn" href="#order">BOOK NOW</a>
  <div class="abs garnish garnish--mushroom" role="img" aria-label="Sliced mushrooms"></div>
  <div class="abs garnish garnish--tomato" role="img" aria-label="Halved cherry tomato"></div>
  <div class="abs shipping">
    <div class="shipping__label">FREE SHIPPING</div>
    <div class="shipping__price">$29.99</div>
  </div>
</section>

<section class="story">
</section>
<div class="abs story__orange-left"></div>
<div class="abs story__orange-right"></div>
<div class="abs frame-square"></div>
<div class="abs frame-tilt"></div>
<h2 class="abs story__heading">
  <span class="story__kicker">OPENING IT’S</span>
  <span class="story__title">DOORS IN JANUARY <em>OF 2010</em></span>
</h2>
<div class="abs story__text">
  <p class="story__lead">Brindleys European Deli was a sandwich shop in Maplecove, New Harbour, but also a lot more than that.</p>
  <p>We spent five years with this business until it’s eventual closure in April of 2015. It was a special time where we met tons of amazing people, who we loved to see and serve.</p>
  <p>Brindleys started out as a deli but eventually morphed into the sandwich shop we all know it as today.</p>
  <p>We are overwhelmed with the continuous positive messages and commentswe get on our Chatterbox page that is still up and running.</p>
  <p>Unfortunately, we can’t open another Brindleys, but we can offer you this collection of our recipes for you to try out at home with your family and friends.</p>
  <p>We truly hope you will enjoy making these sandwiches just as much as we did.</p>
  <p>If you do, please post your pictures of you making a meal or the finished product, or even enjoying it!</p>
</div>
<div class="abs burger" role="img" aria-label="Cheeseburger with lettuce, tomato and crispy onions"></div>

<footer class="footer">Copyright © 2022 Brindleys Sandwich. All Rights Reserved.</footer>
</body>
</html>
```